design a beautiful, neat and professional looking 10 page templete for an online course

I designed an online course. It about the newborn adoption process. I need you to design the template for it. Just the first 10 pages is enough. I'm thinking a neutral palette with a pop of a minor color to keep it from being boring. The pop of color should not distract the reader. You can design how you want. If you want to add small details or hearts or a shape in background you can. Just dont overdo it. Sparingly is the key. You can make pages a different color. It just needs to look like a neutral color palette with a small pop of color.
Updates

Low design quality

Target Market(s)

people who are adopting a newborn in the USA

Industry/Entity Type

newborn adoption

Font styles to use
Sans Serif

Colors

Designer to choose colors to be used in the design.

Requirements
Should not have
• bold or distracting colors or patterns

```html
<!DOCTYPE html>
<html lang="en">
<head>
<meta charset="utf-8">
<title>Newborn Adoption Process – Course Slide Template</title>
<link href="https://fonts.googleapis.com/css2?family=Source+Sans+3:ital,wght@0,300;0,400;0,600;0,700;0,900;1,300&display=swap" rel="stylesheet">
<style>
:root{
  --beige:#d8c4b7;
  --beige-deep:#c7a897;
  --taupe:#8b6a57;
  --slate:#5d6a70;
  --slate-soft:#aab5bd;
  --panel:#f0f0f0;
  --ink:#2f2f2f;
  --text:#5a5a5a;
  --muted:#a3a3a3;
  --white:#ffffff;
}
*{margin:0;padding:0;box-sizing:border-box}
html,body{width:1200px;height:2194px;overflow:hidden;background:var(--white)}
body{position:relative;font-family:"Source Sans 3",sans-serif;color:var(--text)}
.slide{position:absolute;width:420px;height:236px;overflow:hidden;background:var(--white);box-shadow:0 8px 22px rgba(0,0,0,.18)}
.col-l{left:108px}.col-r{left:667px}
.abs{position:absolute}
.photo{position:absolute}
.title{font-weight:900;color:var(--ink);line-height:1.1;text-transform:uppercase;font-size:13px;letter-spacing:.2px}
.sub{font-style:italic;font-weight:300;font-size:10px;color:var(--text)}
.sub::after{content:"";display:block;width:22px;height:1px;background:var(--muted);margin-top:4px}
.body{font-size:5.3px;line-height:1.95;color:var(--muted);text-align:justify}
.num{position:absolute;left:10px;bottom:7px;font-size:4.5px;color:var(--muted);font-weight:700}
.side{position:absolute;top:0;left:0;width:130px;height:100%;background:var(--panel)}
.strip-l{position:absolute;left:0;top:0;width:5px;height:100%;background:var(--beige)}
.strip-r{position:absolute;right:0;top:0;width:5px;height:100%;background:var(--beige)}
.frame{position:absolute;border:3px solid var(--beige)}
.col-card{width:82px}
.col-head{background:var(--beige-deep);color:#fff;font-weight:900;font-size:10px;text-align:center;padding:4px 0}
.col-text{background:rgba(255,255,255,.55);height:105px;padding:10px 6px;font-size:5.3px;line-height:2;color:var(--text)}
</style>
</head>
<body>

<!-- 1 Cover -->
<section class="slide col-l" style="top:47px">
  <div class="photo" role="img" aria-label="Photo of a parent cradling a sleeping newborn" style="left:0;top:0;width:265px;height:236px;background:linear-gradient(135deg,#5a4a45,#b08a78 55%,#8c7870)"></div>
  <div class="photo" role="img" aria-label="Soft faded photo of a mother" style="left:265px;top:0;width:155px;height:236px;background:linear-gradient(180deg,#efe6df,#f7f2ee)"></div>
  <h1 class="abs" style="left:280px;top:66px;font-size:23px;font-weight:900;color:var(--ink);line-height:1.35">Newborn<br>Adoption<br>Process.</h1>
  <p class="abs" style="left:280px;top:176px;font-size:10.5px;font-weight:300;color:var(--text)">Online course.</p>
  <p class="abs" style="left:280px;top:217px;font-size:5.5px;color:var(--text)">City Name , April 4 2024</p>
</section>

<!-- 2 Introduction -->
<section class="slide col-r" style="top:47px;background:var(--beige)">
  <p class="body abs" style="left:12px;top:22px;width:150px;color:#b9a293">Typesetting industry. Lorem ipsum has been the industry's standard dummy text ever since the 1500s, when an unknown printer took a galley of type and scrambled it to make a type specimen book. It has survived not only five centuries, but also the leap into electronic typesetting, remaining essentially unchanged. It was popularised in the 1960s with the release of sample sheets containing Lorem Ipsum passages, and more recently with desktop layout software including versions of lorem ipsum.</p>
  <div class="photo" role="img" aria-label="Photo of a sleeping baby beside a teddy bear" style="left:188px;top:0;width:232px;height:154px;background:linear-gradient(135deg,#e6e4e2,#cfc7c2 60%,#a98a70)"></div>
  <div class="abs" style="left:169px;top:16px;width:226px;height:147px;border:3px solid var(--slate)"></div>
  <h2 class="abs" style="left:184px;top:168px;font-size:24px;font-weight:900;color:var(--ink)">Introduction</h2>
  <p class="abs" style="left:184px;top:197px;font-size:10px;font-weight:300;color:var(--text)">Course Overview</p>
  <p class="num" style="color:#b9a293">SLIDE / 2</p>
</section>

<!-- 3 Information -->
<section class="slide col-l" style="top:312px;background:#f3f3f3">
  <div class="photo" role="img" aria-label="Photo of smiling parents holding their baby" style="left:0;top:0;width:164px;height:236px;background:linear-gradient(135deg,#e8ded6,#8b6c5e 60%,#4d5766)"></div>
  <div class="frame" style="left:12px;top:35px;width:258px;height:158px"></div>
  <h2 class="abs" style="left:82px;top:134px;font-size:22px;font-weight:900;color:var(--ink)">INFORMATION</h2>
  <p class="abs" style="left:188px;top:166px;font-size:10px;font-weight:300">___ Overwiev</p>
  <p class="body abs" style="left:281px;top:33px;width:124px">Typesetting industry. Lorem ipsum has been the industry's standard dummy text ever since the 1500s, when an unknown printer took a galley of type and scrambled it to make a type specimen book. It has survived not only five centuries, but also the leap into electronic typesetting, remaining essentially unchanged. It was popularized in the 1960s with the release of sample sheets containing Lorem Ipsum passages, and more recently with desktop layout software including versions of lorem ipsum.</p>
  <p class="num" style="left:auto;right:20px">SLIDE / 3</p>
</section>

<!-- 4 Laughter -->
<section class="slide col-r" style="top:312px">
  <div class="side"></div>
  <h2 class="title abs" style="left:14px;top:11px">Laughter</h2>
  <p class="sub abs" style="left:14px;top:28px">Subtitle slide here</p>
  <p class="body abs" style="left:14px;top:50px;width:112px">Lorem ipsum is simply dummy text of the printing and typesetting industry. Lorem ipsum has been the industry's standard dummy text ever since the 1500s, when an unknown printer took a galley of type and scrambled it to make a type specimen book. It has survived not only five centuries, but also the leap into electronic typesetting, remaining essentially unchanged. It was popularized in the 1960s with the release of sample sheets containing Lorem Ipsum passages, and more recently with desktop layout software including versions of Lorem Ipsum.</p>
  <svg class="abs" style="left:180px;top:15px" width="210" height="210" viewBox="-105 -105 210 210">
    <path d="M-4,-4 L-4,-70 A66,66 0 0 0 -70,-4 Z" fill="var(--taupe)"/>
    <path d="M4,-4 L4,-70 A66,66 0 0 1 70,-4 Z" fill="var(--slate)"/>
    <path d="M-4,4 L-70,4 A66,66 0 0 0 -4,70 Z" fill="#c9cdd0"/>
    <path d="M4,4 L70,4 A66,66 0 0 1 4,70 Z" fill="var(--beige-deep)"/>
    <g fill="none" stroke-width="7">
      <path d="M-82,-8 A82,82 0 0 1 -10,-82" stroke="var(--taupe)"/>
      <path d="M8,-82 A82,82 0 0 1 82,-10" stroke="var(--slate)"/>
      <path d="M-8,82 A82,82 0 0 1 -82,10" stroke="var(--slate)"/>
      <path d="M82,8 A82,82 0 0 1 10,82" stroke="var(--beige-deep)"/>
    </g>
    <polygon points="-10,-92 6,-82 -10,-72" fill="var(--taupe)"/>
    <polygon points="72,-10 82,6 92,-10" fill="var(--slate)"/>
    <polygon points="-92,10 -82,-6 -72,10" fill="var(--slate)"/>
    <polygon points="10,92 -6,82 10,72" fill="var(--beige-deep)"/>
    <g font-size="3.4" font-family="Source Sans 3, sans-serif" fill="#f3ece7">
      <text x="-58" y="-52">DULorem Ipsum</text><text x="-58" y="-44">Short note about this step</text><text x="-58" y="-38">of the process goes here</text>
      <text x="20" y="-52">DULorem Ipsum</text><text x="14" y="-44">Short note about this step</text><text x="14" y="-38">of the process goes here</text>
      <text x="-58" y="22" fill="#f8f8f8">DULorem Ipsum</text><text x="-58" y="30" fill="#f8f8f8">Short note about this step</text>
      <text x="20" y="22">DULorem Ipsum</text><text x="14" y="30">Short note about this step</text>
    </g>
  </svg>
  <div class="abs" style="left:371px;top:190px;width:38px;height:38px;border:3px solid var(--slate)"></div>
  <p class="num">SLIDE / 4</p>
</section>

<!-- 5 You decide -->
<section class="slide col-l" style="top:577px">
  <div class="photo" role="img" aria-label="Photo of a couple holding their newborn" style="left:0;top:0;width:420px;height:236px;background:linear-gradient(90deg,#aab5bd 0 40%,#c8c9c8 40%,#d9d7d4 70%,#b9b8b6)"></div>
  <div class="abs" style="left:0;top:0;width:165px;height:236px;background:var(--slate-soft)"></div>
  <div class="frame" style="left:12px;top:14px;width:183px;height:206px"></div>
  <h2 class="title abs" style="left:24px;top:36px">You decide</h2>
  <p class="body abs" style="left:24px;top:58px;width:125px;color:#53606a;text-align:left">Lorem ipsum is simply dummy text of the printing and typesetting industry. Lorem Ipsum has been the industry's standard dummy text ever since the 1500s, when an unknown printer took a galley of type and scrambled it to make a type specimen book. It has survived not only five centuries, but also the leap into electronic typesetting, remaining essentially unchanged. It was popularized in the 1960s with the release of sample sheets containing Lorem Ipsum passages, and more recently with desktop layout software including versions of Lorem Ipsum.</p>
  <svg class="abs" style="left:352px;top:6px" width="56" height="56" viewBox="0 0 56 56">
    <circle cx="28" cy="28" r="24" fill="none" stroke="#fff" stroke-width="1.2" stroke-dasharray="100 20"/>
    <circle cx="7" cy="20" r="2.5" fill="#fff"/><circle cx="46" cy="44" r="2.5" fill="none" stroke="#fff"/>
    <text x="28" y="37" text-anchor="middle" font-size="27" font-weight="900" fill="#fff" font-family="Source Sans 3, sans-serif">1</text>
  </svg>
</section>

<!-- 6 You decide columns -->
<section class="slide col-r" style="top:577px">
  <div class="photo" role="img" aria-label="Soft warm photo of a family with a baby" style="left:0;top:0;width:420px;height:236px;background:linear-gradient(90deg,#c9a89a,#d9b9ac 40%,#e6cfc6 70%,#dfc2b3)"></div>
  <h2 class="title abs" style="left:12px;top:11px;color:#fff">You decide</h2>
  <p class="sub abs" style="left:12px;top:28px;color:#fff">Subtitle slide here</p>
  <div class="abs" style="left:25px;top:72px;display:flex;gap:14px">
    <div class="col-card"><div class="col-head">SUBTITLED</div><p class="col-text">Lorem ipsum dolor sit amet, consectetur adipiscing elit. Morbi libero sapien, cursus eget lorem at, convallis hendrerit tortor. Duis vulputate pellentesque dui eget ornare. Aliquam dignissim placerat auctor.</p></div>
    <div class="col-card"><div class="col-head">SUBTITLED</div><p class="col-text">Lorem ipsum dolor sit amet, consectetur adipiscing elit. Morbi libero sapien, cursus eget lorem at, convallis hendrerit tortor. Duis vulputate pellentesque dui eget ornare. Aliquam dignissim placerat auctor.</p></div>
    <div class="col-card"><div class="col-head">SUBTITLED</div><p class="col-text">Lorem ipsum dolor sit amet, consectetur adipiscing elit. Morbi libero sapien, cursus eget lorem at, convallis hendrerit tortor. Duis vulputate pellentesque dui eget ornare. Aliquam dignissim placerat auctor.</p></div>
    <div class="col-card"><div class="col-head">SUBTITLED</div><p class="col-text">Lorem ipsum dolor sit amet, consectetur adipiscing elit. Morbi libero sapien, cursus eget lorem at, convallis hendrerit tortor. Duis vulputate pellentesque dui eget ornare. Aliquam dignissim placerat auctor.</p></div>
  </div>
</section>

<!-- 7 What's the difference – steps -->
<section class="slide col-l" style="top:842px">
  <div class="side"></div><div class="strip-l"></div>
  <h2 class="title abs" style="left:15px;top:85px">What's the<br>difference?</h2>
  <p class="sub abs" style="left:15px;top:118px">Subtitle slide here</p>
  <svg class="abs" style="left:145px;top:45px" width="255" height="150" viewBox="0 0 255 150">
    <g font-family="Source Sans 3, sans-serif">
      <rect x="0" y="0" width="2.5" height="24" fill="#e6d8cf"/><rect x="0" y="24" width="2.5" height="24" fill="var(--beige)"/><rect x="0" y="48" width="2.5" height="24" fill="var(--beige-deep)"/><rect x="0" y="72" width="2.5" height="24" fill="#a88675"/><rect x="0" y="96" width="2.5" height="24" fill="var(--taupe)"/><rect x="0" y="120" width="2.5" height="24" fill="#3b2f29"/>
      <g stroke="#dcdcdc" stroke-width=".6"><line x1="8" y1="24" x2="255" y2="24"/><line x1="8" y1="48" x2="255" y2="48"/><line x1="8" y1="72" x2="255" y2="72"/><line x1="8" y1="96" x2="255" y2="96"/><line x1="8" y1="120" x2="255" y2="120"/><line x1="8" y1="144" x2="255" y2="144"/></g>
      <g font-size="6.5" font-weight="700" fill="var(--ink)"><text x="10" y="14">STEP</text><text x="10" y="38">STEP</text><text x="10" y="62">STEP</text><text x="10" y="86">STEP</text><text x="10" y="110">STEP</text><text x="10" y="134">STEP</text></g>
      <g font-size="3.6" fill="var(--muted)">
        <text x="40" y="11">Duis vulputate pellentesque dui eget ornare. Aliquam dignissim placerat auctor. Lorem ipsum dolor sit</text><text x="40" y="17">amet, consectetur adipiscing elit. Morbi libero sapien, cursus eget lorem at, convallis hendrerit tortor.</text>
        <text x="40" y="35">Duis vulputate pellentesque dui eget ornare. Aliquam dignissim placerat auctor. Lorem ipsum dolor sit</text><text x="40" y="41">amet, consectetur adipiscing elit. Morbi libero sapien, cursus eget lorem at, convallis hendrerit tortor.</text>
        <text x="40" y="59">Duis vulputate pellentesque dui eget ornare. Aliquam dignissim placerat auctor. Lorem ipsum dolor sit</text><text x="40" y="65">amet, consectetur adipiscing elit. Morbi libero sapien, cursus eget lorem at, convallis hendrerit tortor.</text>
        <text x="40" y="83">Duis vulputate pellentesque dui eget ornare. Aliquam dignissim placerat auctor. Lorem ipsum dolor sit</text><text x="40" y="89">amet, consectetur adipiscing elit. Morbi libero sapien, cursus eget lorem at, convallis hendrerit tortor.</text>
        <text x="40" y="107">Duis vulputate pellentesque dui eget ornare. Aliquam dignissim placerat auctor. Lorem ipsum dolor sit</text><text x="40" y="113">amet, consectetur adipiscing elit. Morbi libero sapien, cursus eget lorem at, convallis hendrerit tortor.</text>
        <text x="40" y="131">Duis vulputate pellentesque dui eget ornare. Aliquam dignissim placerat auctor. Lorem ipsum dolor sit</text><text x="40" y="137">amet, consectetur adipiscing elit. Morbi libero sapien, cursus eget lorem at, convallis hendrerit tortor.</text>
      </g>
    </g>
  </svg>
  <p class="num">SLIDE / 7</p>
</section>

<!-- 8 What's the difference – text -->
<section class="slide col-r" style="top:842px">
  <div class="side"></div><div class="strip-l"></div>
  <h2 class="title abs" style="left:15px;top:85px">What's the<br>difference?</h2>
  <p class="sub abs" style="left:15px;top:118px">Subtitle slide here</p>
  <p class="body abs" style="left:160px;top:42px;width:225px">Typesetting industry. Lorem ipsum has been the industry's standard dummy text ever since the 1500s, when an unknown printer took a galley of type and scrambled it to make a type specimen book. It has survived not only five centuries, but also the leap into electronic typesetting, remaining essentially unchanged. It was popularized in the 1960s with the release of sample sheets containing.</p>
  <p class="body abs" style="left:160px;top:130px;width:225px">Typesetting industry. Lorem ipsum has been the industry's standard dummy text ever since the 1500s, when an unknown printer took a galley of type and scrambled it to make a type specimen book. It has survived not only five centuries, but also the leap into electronic typesetting, remaining essentially unchanged. It was popularized in the 1960s with the release of sample sheets containing.</p>
  <p class="num">SLIDE / 8</p>
</section>

<!-- 9 Money as a right -->
<section class="slide col-l" style="top:1107px">
  <div class="abs" style="left:255px;top:0;width:160px;height:236px;background:var(--panel)"></div><div class="strip-r"></div>
  <ul class="body abs" style="left:24px;top:40px;width:210px;padding-left:8px;line-height:2.3">
    <li>Typesetting industry. Lorem ipsum has been the industry's standard dummy text ever since the 1500s, when an unknown printer took a galley of type</li>
    <li>And scrambled it to make a type specimen book. It has survived not only five centuries, but also the leap into electronic typesetting, remaining essentially unchanged. It was popularized in the 1960s with the release of sample sheets containing.</li>
    <li>Typesetting industry. Lorem ipsum has been the industry's standard dummy text ever since the 1500s, when an unknown printer took a galley of type</li>
    <li>And scrambled it to make a type specimen book. It has survived not only five centuries, but also the leap into electronic typesetting, remaining essentially unchanged. It was popularized in the 1960s with the release of sample sheets containing.</li>
  </ul>
  <h2 class="title abs" style="left:285px;top:85px">Money as<br>a “right.”</h2>
  <p class="sub abs" style="left:285px;top:118px">Subtitle slide here</p>
  <p class="num" style="left:auto;right:26px">SLIDE / 9</p>
</section>

<!-- 10 Here's how -->
<section class="slide col-r" style="top:1107px">
  <div class="side"></div><div class="strip-l"></div>
  <h2 class="title abs" style="left:15px;top:101px">Here's how:</h2>
  <p class="sub abs" style="left:15px;top:118px">Subtitle slide here</p>
  <p class="body abs" style="left:180px;top:40px;width:205px">Typesetting industry. Lorem ipsum has been the industry's standard dummy text ever since the 1500s, when an unknown printer took a galley of type and scrambled it to make a type specimen book. It has survived not only five centuries, but also the leap into electronic typesetting, remaining essentially unchanged. It was popularized in the 1960s with the release of sample sheets containing.</p>
  <p class="body abs" style="left:180px;top:128px;width:205px">Typesetting industry. Lorem ipsum has been the industry's standard dummy text ever since the 1500s, when an unknown printer took a galley of type and scrambled it to make a type specimen book. It has survived not only five centuries, but also the leap into electronic typesetting, remaining essentially unchanged. It was popularized in the 1960s with the release of sample sheets containing.</p>
  <p class="num">SLIDE / 10</p>
</section>

<!-- 11 Section divider -->
<section class="slide col-l" style="top:1372px">
  <div class="photo" role="img" aria-label="Photo of parents playing with a baby on a bed" style="left:0;top:0;width:420px;height:236px;background:linear-gradient(135deg,#9c8f86,#c7bdb5 45%,#a99a90 75%,#8d8078)"></div>
  <div class="abs" style="left:10px;top:10px;width:400px;height:216px;border:1px solid rgba(255,255,255,.35)"></div>
  <h2 class="abs" style="left:75px;top:160px;font-size:29px;font-weight:900;color:#fff">SECTION SLIDE</h2>
  <p class="abs" style="left:273px;top:195px;font-size:9px;font-weight:300;color:#fff">Divider</p>
  <div class="abs" style="left:325px;top:145px;width:88px;height:89px;border:3px solid var(--slate)"></div>
  <p class="abs" style="left:336px;top:160px;font-size:50px;line-height:1;font-weight:400;color:#fff">01</p>
</section>

<!-- 12 Perception chart -->
<section class="slide col-r" style="top:1372px">
  <div class="side"></div>
  <h2 class="title abs" style="left:14px;top:10px">Perception<br>chart</h2>
  <p class="sub abs" style="left:14px;top:44px">Subtitle slide here</p>
  <p class="body abs" style="left:14px;top:68px;width:110px">Typesetting industry. Lorem ipsum has been the industry's standard dummy text ever since the 1500s, when an unknown printer took a galley of type and scrambled it to make a type specimen book. It has survived not only five centuries, but also the leap into electronic typesetting, remaining essentially unchanged. It was popularized in the 1960s with the release of sample sheets containing.</p>
  <svg class="abs" style="left:148px;top:33px" width="260" height="190" viewBox="0 0 260 190" font-family="Source Sans 3, sans-serif">
    <rect x="0" y="0" width="260" height="16" fill="var(--beige-deep)"/>
    <g font-size="4" font-weight="700" fill="#fff" text-anchor="middle"><text x="78" y="10">COLUMN 1</text><text x="130" y="10">COLUMN 2</text><text x="182" y="10">COLUMN 3</text><text x="234" y="10">COLUMN 4</text></g>
    <g fill="#ececec"><rect y="16" width="260" height="17"/><rect y="50" width="260" height="17"/><rect y="84" width="260" height="17"/><rect y="118" width="260" height="17"/><rect y="152" width="260" height="17"/></g>
    <g stroke="#fff" stroke-width="1"><line x1="52" y1="0" x2="52" y2="190"/><line x1="104" y1="0" x2="104" y2="190"/><line x1="156" y1="0" x2="156" y2="190"/><line x1="208" y1="0" x2="208" y2="190"/></g>
    <rect y="170" width="260" height="17" fill="#555"/>
    <g font-size="4" fill="var(--ink)">
      <g font-weight="700"><text x="3" y="27">Row Sample 01</text><text x="3" y="44">Row Sample 02</text><text x="3" y="61">Row Sample 03</text><text x="3" y="78">Row Sample 04</text><text x="3" y="95">Row Sample 05</text><text x="3" y="112">Row Sample 06</text><text x="3" y="129">Row Sample 07</text><text x="3" y="146">Row Sample 08</text><text x="3" y="163">Row Sample 09</text></g>
      <g text-anchor="middle">
        <text x="78" y="27">328</text><text x="130" y="27">368</text><text x="182" y="27">388</text><text x="234" y="27">408</text>
        <text x="78" y="44">285</text><text x="130" y="44">325</text><text x="182" y="44">345</text><text x="234" y="44">365</text>
        <text x="78" y="61">256</text><text x="130" y="61">296</text><text x="182" y="61">316</text><text x="234" y="61">336</text>
        <text x="78" y="78">123</text><text x="130" y="78">163</text><text x="182" y="78">183</text><text x="234" y="78">203</text>
        <text x="78" y="95">532</text><text x="130" y="95">572</text><text x="182" y="95">592</text><text x="234" y="95">612</text>
        <text x="78" y="112">256</text><text x="130" y="112">296</text><text x="182" y="112">316</text><text x="234" y="112">336</text>
        <text x="78" y="129">985</text><text x="130" y="129">1025</text><text x="182" y="129">1045</text><text x="234" y="129">1065</text>
        <text x="78" y="146">645</text><text x="130" y="146">685</text><text x="182" y="146">705</text><text x="234" y="146">725</text>
        <text x="78" y="163">766</text><text x="130" y="163">806</text><text x="182" y="163">826</text><text x="234" y="163">846</text>
      </g>
    </g>
    <g font-size="4" font-weight="700" fill="#fff"><text x="3" y="181">Total Row</text><g text-anchor="middle"><text x="78" y="181">4176</text><text x="130" y="181">4336</text><text x="182" y="181">4536</text><text x="234" y="181">4716</text></g></g>
  </svg>
  <p class="num">SLIDE / 12</p>
</section>

<!-- 13 Timeline start -->
<section class="slide col-l" style="top:1637px">
  <div class="side"></div><div class="strip-l"></div>
  <h2 class="title abs" style="left:15px;top:66px">Newborn<br>adoption<br>process</h2>
  <p class="sub abs" style="left:15px;top:112px">Subtitle slide here</p>
  <p class="body abs" style="left:15px;top:136px;width:108px;text-align:left">Lorem ipsum dolor sit amet, consectetur adipiscing elit. Morbi libero sapien, cursus eget lorem at, convallis hendrerit tortor. Duis vulputate pellentesque dui eget ornare. Aliquam dignissim placerat auctor.</p>
  <svg class="abs" style="left:130px;top:0" width="290" height="236" viewBox="0 0 290 236" font-family="Source Sans 3, sans-serif">
    <line x1="58" y1="123" x2="290" y2="123" stroke="#cfcfcf" stroke-width="1"/>
    <g stroke="#cfcfcf" stroke-dasharray="2 2" fill="none" stroke-width=".7">
      <polyline points="81,118 70,52 8,52"/><polyline points="157,118 168,52 230,52"/><polyline points="119,128 108,182 82,182"/>
    </g>
    <circle cx="35" cy="123" r="27" fill="var(--beige)" stroke="#dcdcdc" stroke-width="4"/>
    <text x="35" y="124" text-anchor="middle" font-size="15" font-weight="700" fill="var(--ink)">start</text>
    <text x="35" y="134" text-anchor="middle" font-size="6.5" fill="var(--ink)">2024</text>
    <g fill="#fff" stroke="#9aa3a7" stroke-width="1.3"><circle cx="81" cy="123" r="5"/><circle cx="157" cy="123" r="5"/><circle cx="234" cy="123" r="5"/></g>
    <g fill="#fff" stroke="#d8d8d8" stroke-width="1" stroke-dasharray="1.5 1"><circle cx="119" cy="123" r="4.5"/><circle cx="196" cy="123" r="4.5"/><circle cx="272" cy="123" r="4.5"/></g>
    <g font-size="4.5" fill="var(--text)">
      <text transform="translate(83,133) rotate(-70)" text-anchor="end">January</text>
      <text transform="translate(121,133) rotate(-70)" text-anchor="end" fill="#c9c9c9">February</text>
      <text transform="translate(159,133) rotate(-70)" text-anchor="end">March</text>
      <text transform="translate(198,133) rotate(-70)" text-anchor="end" fill="#c9c9c9">April</text>
      <text transform="translate(236,133) rotate(-70)" text-anchor="end">May</text>
      <text transform="translate(274,133) rotate(-70)" text-anchor="end" fill="#c9c9c9">June</text>
    </g>
    <g font-size="5" font-weight="700" fill="var(--ink)"><text x="8" y="48">PHASE 01</text><text x="160" y="48">PHASE 03</text><text x="90" y="178">PHASE 02</text></g>
    <g font-size="3.6" fill="var(--muted)">
      <text x="8" y="60">Morbi libero sapien, cursus</text><text x="8" y="66">eget lorem at, convallis</text><text x="8" y="72">hendrerit tortor</text>
      <text x="160" y="60">Morbi libero sapien, cursus</text><text x="160" y="66">eget lorem at, convallis</text><text x="160" y="72">hendrerit tortor</text>
      <text x="90" y="190">Morbi libero sapien, cursus</text><text x="90" y="196">eget lorem at, convallis</text><text x="90" y="202">hendrerit tortor</text>
    </g>
  </svg>
  <p class="num">SLIDE / 13</p>
</section>

<!-- 14 Timeline end -->
<section class="slide col-r" style="top:1637px">
  <div class="abs" style="left:290px;top:0;width:125px;height:236px;background:var(--panel)"></div><div class="strip-r"></div>
  <svg class="abs" style="left:0;top:0" width="290" height="236" viewBox="0 0 290 236" font-family="Source Sans 3, sans-serif">
    <line x1="0" y1="123" x2="230" y2="123" stroke="#cfcfcf"/>
    <line x1="132" y1="123" x2="228" y2="123" stroke="#b5b5b5" stroke-width="1.5" stroke-dasharray="6 5"/>
    <rect x="132" y="52" width="76" height="143" fill="#f7f7f7" stroke="#bdbdbd" stroke-width=".8" stroke-dasharray="2 2"/>
    <text x="170" y="60" text-anchor="middle" font-size="6" font-weight="700" fill="var(--ink)">ADOPTION</text>
    <text x="170" y="68" text-anchor="middle" font-size="6" font-weight="700" fill="var(--ink)">WAITING TIME</text>
    <line x1="56" y1="90" x2="56" y2="118" stroke="#bdbdbd" stroke-dasharray="1.5 1.5"/>
    <text x="56" y="80" text-anchor="middle" font-size="5" font-weight="700" fill="var(--ink)">SUMMARY</text>
    <text x="56" y="87" text-anchor="middle" font-size="5" font-weight="700" fill="var(--ink)">MEETING</text>
    <g fill="#fff" stroke="#d8d8d8" stroke-dasharray="1.5 1"><circle cx="18" cy="123" r="4.5"/><circle cx="94" cy="123" r="4.5"/></g>
    <circle cx="56" cy="123" r="5.5" fill="var(--slate)" stroke="#c3c8cb" stroke-width="1.5"/>
    <g font-size="4.5" fill="#c9c9c9"><text transform="translate(20,133) rotate(-70)" text-anchor="end">July</text><text transform="translate(58,133) rotate(-70)" text-anchor="end" fill="var(--text)">August</text><text transform="translate(96,133) rotate(-70)" text-anchor="end">September</text></g>
    <circle cx="254" cy="123" r="27" fill="var(--beige)" stroke="#dcdcdc" stroke-width="4"/>
    <text x="254" y="124" text-anchor="middle" font-size="15" font-weight="700" fill="var(--ink)">End</text>
    <text x="254" y="134" text-anchor="middle" font-size="6.5" fill="var(--ink)">2016</text>
  </svg>
  <p class="body abs" style="left:300px;top:98px;width:110px;text-align:left">Lorem ipsum dolor sit amet, consectetur adipiscing elit. Morbi libero sapien, cursus eget lorem at, convallis hendrerit tortor. Duis vulputate pellentesque dui eget ornare. Aliquam dignissim placerat auctor.</p>
  <p class="num" style="left:auto;right:14px">SLIDE / 14</p>
</section>

<!-- 15 Gantt chart -->
<section class="slide col-l" style="top:1902px">
  <div class="photo" role="img" aria-label="Faded photo of parents with a newborn" style="left:0;top:0;width:420px;height:236px;background:linear-gradient(90deg,#e4d7cd,#e7ddd5 45%,#c9c6c3 65%,#dcd8d4)"></div>
  <h2 class="title abs" style="left:18px;top:44px;font-size:14px">Process gant<br>chart</h2>
  <p class="abs" style="left:18px;top:80px;width:130px;font-size:8px;line-height:2;color:#8f7f74">Duis vulputate pellentesque dui eget ornare. Aliquam dignissim placerat auctor. Lorem ipsum dolor sit amet, consectetur adipiscing elit. Morbi libero sapien, cursus eget lorem at, convallis hendrerit tortor.</p>
  <svg class="abs" style="left:160px;top:55px" width="260" height="130" viewBox="0 0 260 130" font-family="Source Sans 3, sans-serif">
    <defs><pattern id="hatch" width="4" height="4" patternUnits="userSpaceOnUse" patternTransform="rotate(45)"><rect width="4" height="4" fill="#7c878c"/><line x1="0" y1="0" x2="0" y2="4" stroke="#aeb6ba" stroke-width="1.5"/></pattern></defs>
    <g font-size="4" fill="var(--text)" text-anchor="middle"><text x="22" y="6">date</text><text x="54" y="6">date</text><text x="86" y="6">date</text><text x="118" y="6">date</text><text x="150" y="6">date</text><text x="182" y="6">date</text><text x="214" y="6">date</text></g>
    <polygon points="5,33 90,33 96,38 90,43 5,43" fill="url(#hatch)"/>
    <polygon points="37,53 122,53 128,58 122,63 37,63" fill="url(#hatch)"/>
    <polygon points="116,73 206,73 212,78 206,83 116,83" fill="url(#hatch)"/>
    <polygon points="210,93 245,93 251,98 245,103 210,103" fill="var(--slate)"/>
    <g font-size="3.5" fill="#fff"><text x="8" y="39.5">Phase one</text><text x="40" y="59.5">Phase two</text><text x="119" y="79.5">Phase three</text><text x="213" y="99.5">Final step</text></g>
  </svg>
</section>

<!-- 16 Thank you -->
<section class="slide col-r" style="top:1902px">
  <div class="photo" role="img" aria-label="Photo of a couple holding their newborn" style="left:0;top:0;width:420px;height:236px;background:linear-gradient(90deg,#d6d7d8,#cfcfce 45%,#b5b2ae 70%,#d2d1cf)"></div>
  <div class="abs" style="left:10px;top:55px;width:135px;height:146px;background:#fff"></div>
  <div class="frame" style="left:10px;top:55px;width:135px;height:146px"></div>
  <h2 class="abs" style="left:21px;top:92px;font-size:16px;font-weight:900;color:var(--beige-deep)">THANK YOU</h2>
  <div class="abs" style="left:21px;top:113px;font-size:5.5px;line-height:1.5;color:var(--text)">
    <p style="font-size:7.5px;font-weight:700;color:var(--taupe)">CONTACT</p>
    <p>Maple Adoption Team</p>
    <p>555 010 2020</p>
    <p>hello@mapleadoption.com</p>
    <p>Company adress</p>
    <p>Willow Lane 21</p>
    <p>40-118 Portland, US</p>
  </div>
  <div class="abs" style="left:124px;top:106px;display:flex;flex-direction:column;gap:8px">
    <span style="display:block;width:9px;height:9px;background:var(--slate)"></span>
    <span style="display:block;width:9px;height:9px;background:var(--slate)"></span>
    <span style="display:block;width:9px;height:9px;background:var(--slate)"></span>
  </div>
</section>

</body>
</html>
```